Bold Modern Creative Wine Label Needed for a Chardonnay

We need a modern, eye catching label, one that will appeal to millennials, but also attract the older more conservative crowd. We like the boldness of black on white but are open to your suggestions. Since the bottle type is a light green 'burgundy style' bottle, you should take that into account. The name of the brand is Vo`. The attached label is example of what we like very much. It is eye catching and bold and modern. Keep in mind that the bottle will be light green in color so black and white might not work so well. Use your creativity please! The label can be any size but needs to fit on this shape bottle. See attached photos. thanks!!

(Please no grapes or wine glasses or wine bottles featured on the label!)
Updates

Hi Designers, I just wanted to let you know that we received many great designs and we are sorting through them this week. The website is making it a bit difficult to create a 'poll' so this is taking longer than we expected. Thanks for all the great submissions!

```html
<!DOCTYPE html>
<html lang="en">
<head>
<meta charset="UTF-8">
<title>Vo` Chardonnay — Wine Label</title>
<link rel="stylesheet" href="https://fonts.googleapis.com/css2?family=Playfair+Display:wght@400;500&family=Oswald:wght@300;400&family=Libre+Baskerville:wght@400&display=swap">
<style>
  :root {
    --backdrop: #e4e4e4;
    --paper: #fbfbfa;
    --ink: #3b3a3a;
    --frame-light: #8a8a8a;
    --wine-red: #a3191f;
    --night: #141414;
    --frame-dark: #5a5a5a;
    --paper-on-night: #f3f3f3;
  }
  * { margin: 0; padding: 0; box-sizing: border-box; }
  html, body {
    width: 1200px;
    height: 800px;
    overflow: hidden;
    background: var(--backdrop);
  }
  .sheet {
    width: 1200px;
    height: 800px;
    display: flex;
    align-items: center;
    justify-content: center;
    gap: 80px;
  }
  .label {
    position: relative;
    width: 380px;
    height: 420px;
    background: var(--paper);
    color: var(--ink);
    box-shadow: 0 2px 6px rgba(0,0,0,0.08);
  }
  .label__frame {
    position: absolute;
    inset: 16px;
    border: 1.5px solid var(--frame-light);
  }
  .label__varietal {
    position: absolute;
    left: 58px;
    top: 56px;
    width: 190px;
    height: 24px;
    transform-origin: 0 0;
    transform: rotate(-90deg) translateX(-190px);
    font-family: "Oswald", sans-serif;
    font-weight: 400;
    font-size: 17px;
    letter-spacing: 3px;
    color: var(--wine-red);
    text-align: center;
    line-height: 24px;
  }
  .label__brand {
    position: absolute;
    left: 86px;
    top: 52px;
    font-family: "Playfair Display", serif;
    font-weight: 400;
    font-size: 150px;
    line-height: 1;
    letter-spacing: -2px;
    color: var(--ink);
  }
  .label__title {
    position: absolute;
    left: 40px;
    top: 262px;
    font-family: "Oswald", sans-serif;
    font-weight: 300;
    font-size: 22px;
    letter-spacing: 0.5px;
    color: var(--wine-red);
  }
  .label__blend {
    position: absolute;
    left: 40px;
    top: 300px;
    list-style: none;
    font-family: "Libre Baskerville", serif;
    font-size: 10px;
    line-height: 13px;
    color: var(--ink);
  }
  .label__vintage {
    position: absolute;
    right: 40px;
    top: 312px;
    font-family: "Playfair Display", serif;
    font-size: 22px;
    color: var(--wine-red);
  }
  .label__volume {
    position: absolute;
    left: 0;
    right: 0;
    bottom: 36px;
    text-align: center;
    font-family: "Libre Baskerville", serif;
    font-size: 12px;
    letter-spacing: 0.5px;
    color: var(--ink);
  }
  .label--night {
    background: var(--night);
    color: var(--paper-on-night);
  }
  .label--night .label__frame { border-color: var(--frame-dark); }
  .label--night .label__brand,
  .label--night .label__blend,
  .label--night .label__volume { color: var(--paper-on-night); }
</style>
</head>
<body>
  <main class="sheet">
    <article class="label label--day">
      <div class="label__frame"></div>
      <div class="label__varietal">CHARDONNAY</div>
      <div class="label__brand">Vo`</div>
      <div class="label__title">PREMIUM WINE</div>
      <ul class="label__blend">
        <li>60% Siraz</li>
        <li>35% Cabernet Sauvignon</li>
        <li>5% Cabernet Franc</li>
      </ul>
      <div class="label__vintage">2019</div>
      <div class="label__volume">750ML. 13.5% ALC/VOL</div>
    </article>

    <article class="label label--night">
      <div class="label__frame"></div>
      <div class="label__varietal">CHARDONNAY</div>
      <div class="label__brand">Vo`</div>
      <div class="label__title">PREMIUM WINE</div>
      <ul class="label__blend">
        <li>60% Siraz</li>
        <li>35% Cabernet Sauvignon</li>
        <li>5% Cabernet Franc</li>
      </ul>
      <div class="label__vintage">2019</div>
      <div class="label__volume">750ML. 13.5% ALC/VOL</div>
    </article>
  </main>
</body>
</html>
```